Stationery Design Project

Letterhead with logo and address
Envelopes with Logo and address

The target market is start-ups and
small to medium businesses primarly located in China, with less than 20
employees. Please have designers use Yellow and Blue colors and our logo
attached. Looking fr the same format as the business card attached.

Reason: Designer has been delayed working on web design

Target Market(s)

Start-ups and small to medium size businesses

Industry/Entity Type

Business

Font styles to use
Sans Serif

Requirements
Must have
• None
Nice to have
• None
Should not have
• N/A

```html
<!DOCTYPE html>
<html lang="en">
<head>
<meta charset="utf-8">
<title>Envelope – Harborline Asset And Property Advisory</title>
<link rel="stylesheet" href="https://fonts.googleapis.com/css2?family=Lato:wght@700;900&display=swap">
<style>
  :root {
    --band-blue: #0b4a7f;
    --ink-blue: #1b4e86;
    --brand-yellow: #f4bb1e;
    --wordmark-blue: #2ea8e8;
    --paper: #ffffff;
    --white: #ffffff;
  }
  html, body {
    margin: 0;
    padding: 0;
    width: 1200px;
    height: 600px;
    overflow: hidden;
    background: var(--paper);
  }
  .envelope {
    position: relative;
    width: 1200px;
    height: 600px;
    background: var(--paper);
    font-family: "Lato", Arial, sans-serif;
  }
  .brand-band {
    position: absolute;
    left: 0;
    top: 0;
    width: 233px;
    height: 600px;
    background: var(--band-blue);
  }
  .brand-mark {
    position: absolute;
    left: 46px;
    top: 50px;
    width: 140px;
    height: 140px;
  }
  .brand-name {
    position: absolute;
    left: 0;
    top: 230px;
    width: 233px;
    margin: 0;
    text-align: center;
    font-weight: 700;
    font-size: 31px;
    letter-spacing: 9px;
    padding-left: 9px;
    box-sizing: border-box;
    color: var(--wordmark-blue);
  }
  .website {
    position: absolute;
    left: 0;
    bottom: 26px;
    width: 233px;
    margin: 0;
    text-align: center;
    font-weight: 700;
    font-size: 15.5px;
    color: var(--white);
  }
  .sender {
    position: absolute;
    left: 257px;
    top: 72px;
    color: var(--ink-blue);
    font-weight: 900;
    font-size: 18px;
    line-height: 18.5px;
  }
  .sender p {
    margin: 0 0 11px;
  }
</style>
</head>
<body>
  <main class="envelope">
    <aside class="brand-band">
      <svg class="brand-mark" viewBox="0 0 140 140" aria-hidden="true">
        <circle cx="70" cy="70" r="70" fill="var(--brand-yellow)"/>
      </svg>
      <p class="brand-name">HAPA</p>
      <p class="website">www.hapachina.com</p>
    </aside>
    <address class="sender" style="font-style: normal;">
      <p class="company-name">Harborline Asset And<br>Property Advisory Consulting<br>(Shanghai) Co., Ltd.</p>
      <p class="street-address">Lanting Road 58, suite 210-212<br>Minhang Dist., Shanghai</p>
    </address>
  </main>
</body>
</html>
```